Website Design for a holiday home letting busines

We require a redesign of our present website www.birchwoodstays.com. We want the website to stand out and look professional and clean to make holiday hunters want to book a caravan or lodge holiday with us. Our logo is red however we DO NOT want the website to be red. We want a natural colour scheme.

The final design should communicate that we are a professional company to book with.

On the home page we require;
Overview of company
Photo
Search box for holiday (check in)
Late Deals
Reviews
News

We would like the following pages designed; home page, available dates page, caravans page, content page.

The website should be responsive for smart phones. One website I do like is http://www.verdamoro.be/nl/

Target Market(s)

Families

Industry/Entity Type

Travel

Number of Pages Required

5+ page

Font styles to use
Serif

Requirements
Must have
• The project must be responsive for mobile phones and tablets.
• Ability to search for holiday home holidays
• We want a natural colour scheme.
Nice to have
• A style we like is http://www.verdamoro.be/nl/
Should not have
• Do not use red as a colour for the website. Our logo is red so this is the only time we want this used.

```html
<!DOCTYPE html>
<html lang="en">
<head>
<meta charset="utf-8">
<title>Birchwood Stays – Private Holiday Rentals</title>
<link rel="stylesheet" href="https://fonts.googleapis.com/css2?family=Open+Sans:wght@400;600;700&display=swap">
<style>
:root{
  --accent:#5f7f3c;
  --accent-dark:#4a662d;
  --accent-soft:#e9efe0;
  --ink:#333a42;
  --muted:#858b92;
  --line:#e2e5e0;
  --pale:#f2f6f1;
  --footer:#2d3530;
  --footer-deep:#232a26;
  --white:#ffffff;
}
*{box-sizing:border-box;margin:0;padding:0}
html,body{width:1200px;height:3772px;overflow:hidden}
body{font-family:"Open Sans",Arial,sans-serif;color:var(--ink);background:var(--white);font-size:12px;line-height:1.5}
a{color:inherit;text-decoration:none}
.container{width:900px;margin:0 auto;position:relative}
h2.section-title{font-weight:400;font-size:30px;text-align:center;color:var(--ink)}

/* top bar */
.topbar{height:32px;border-bottom:1px solid var(--line);font-size:11px;color:var(--muted)}
.topbar .container{display:flex;justify-content:flex-end;align-items:center;height:32px;gap:24px}
.topbar span{display:flex;align-items:center;gap:6px}

/* nav */
.site-nav{height:56px}
.site-nav .container{display:flex;align-items:center;justify-content:space-between;height:56px}
.brand{display:flex;align-items:center;gap:8px;font-weight:700;font-size:16px;color:var(--ink)}
.brand .mark{width:22px;height:22px;border-radius:50%;background:var(--accent)}
.menu{display:flex;gap:22px;font-size:11px;color:var(--ink)}
.menu a.active{color:var(--accent)}

/* hero */
.hero{height:500px;position:relative;background:linear-gradient(180deg,#a9c5cf 0%,#7e9b8f 40%,#4f6c5e 70%,#6b5a49 100%);text-align:center;color:var(--white)}
.hero-photo{position:absolute;inset:0}
.hero-content{position:relative;padding-top:150px}
.hero h1{font-weight:700;font-size:44px;text-shadow:0 2px 6px rgba(0,0,0,.3)}
.hero p{font-size:13px;margin-top:8px;opacity:.95}
.btn{display:inline-block;background:var(--accent);color:var(--white);font-weight:700;font-size:11px;text-transform:uppercase;letter-spacing:.5px;padding:10px 28px;border-radius:2px}
.hero .btn{margin-top:34px}

/* search */
.search-bar{position:absolute;left:50%;top:565px;transform:translateX(-50%);width:920px;height:50px;background:var(--white);box-shadow:0 3px 12px rgba(0,0,0,.12);display:flex;align-items:center;padding:0 10px;gap:8px;z-index:2}
.search-field{flex:1;height:32px;border-right:1px solid var(--line);display:flex;align-items:center;justify-content:space-between;padding:0 10px;font-size:11px;color:var(--muted)}
.search-field.wide{flex:2.2}
.search-bar .btn{padding:9px 22px}

/* about */
.about{height:442px;padding-top:92px}
.about .container{display:flex;gap:40px}
.about-art{width:470px;height:260px;background:linear-gradient(135deg,#dff0f7,#bfe0ee 60%,#f4d7a8);border-radius:2px}
.about-text{flex:1;padding-top:6px}
.about-text h2{font-weight:400;font-size:30px}
.about-text h3{color:var(--accent);font-size:13px;font-weight:600;margin:6px 0 12px}
.about-text p{color:var(--muted);font-size:11.5px;margin-bottom:10px;line-height:1.7}
.about-text .btn{margin-top:8px;padding:8px 18px}

/* listings */
.listings{height:640px;background:var(--pale);padding-top:50px}
.cards{display:flex;gap:30px;margin-top:55px}
.card{width:280px;background:var(--white);box-shadow:0 2px 8px rgba(0,0,0,.06);position:relative}
.card-photo{height:160px}
.price{position:absolute;right:0;top:132px;background:var(--accent);color:var(--white);font-weight:700;font-size:12px;padding:6px 12px}
.card-body{padding:14px 16px 16px}
.card-body h4{font-size:12px;font-weight:600}
.card-body .addr{color:var(--accent);font-size:10.5px;margin-top:2px}
.specs{display:grid;grid-template-columns:1fr 1fr;gap:6px 10px;margin-top:12px;font-size:10.5px;color:var(--muted)}
.specs span{display:flex;align-items:center;gap:6px}
.specs b{color:var(--ink);font-weight:600}
.listings .more{text-align:center;margin-top:34px}
.listings .more .btn{padding:12px 36px}

/* late deals */
.deals{height:620px;padding-top:80px}
.deals .cards{margin-top:40px}
.deals .card{box-shadow:none}
.deals .card-body{padding:12px 4px}
.deals .card-body .date{font-size:11px;font-weight:600}
.deals .btn{margin-top:14px;font-size:10px;padding:8px 14px}

/* reviews */
.reviews{height:490px;background:var(--pale);padding-top:72px}
.tabs{display:flex;justify-content:center;margin-top:28px;font-size:10.5px;color:var(--muted)}
.tabs span{padding:6px 20px;border-bottom:2px solid var(--line)}
.tabs span.active{color:var(--ink);border-bottom-color:var(--accent)}
.review{display:flex;gap:40px;margin-top:52px;padding-left:110px}
.review-photo{width:220px;height:200px;background:linear-gradient(160deg,#9fc6e0,#e2c7a8)}
.review-text{width:400px;padding-top:14px;color:var(--muted);font-size:11.5px;line-height:1.7}
.review-text .who{color:var(--ink);font-weight:600;margin-top:14px}
.stars{display:flex;gap:6px;margin-top:12px}
.stars i{width:14px;height:14px;border-radius:50%;border:1px solid #c8cdc6}

/* blog */
.blog{height:680px;padding-top:92px}
.blog .cards{margin-top:52px}
.blog .card{box-shadow:none}
.blog .card-photo{height:180px}
.blog .card-body{padding:12px 2px}
.blog h4{font-size:12.5px}
.blog .meta{font-size:10px;color:var(--muted)}
.blog .excerpt{font-size:10.5px;color:var(--muted);margin-top:8px;line-height:1.6}
.blog .read{color:var(--accent);font-size:10.5px;margin-top:8px;display:block}

/* footer */
.site-footer{height:312px;background:var(--footer);color:#c4cac4;position:relative}
.newsletter{text-align:center;padding-top:40px}
.newsletter h3{font-weight:400;font-size:22px;color:var(--white)}
.subscribe{display:flex;width:400px;margin:16px auto 0;height:34px}
.subscribe .input{flex:1;background:var(--white);border-radius:17px 0 0 17px;display:flex;align-items:center;padding-left:16px;color:var(--muted);font-size:11px}
.subscribe .btn{border-radius:0 17px 17px 0;padding:10px 20px}
.footer-cols{display:flex;justify-content:space-between;margin-top:36px;font-size:11px}
.footer-cols h5{color:var(--white);font-size:12px;margin-bottom:6px}
.footer-cols li{list-style:none;line-height:1.7}
.follow{display:flex;align-items:center;gap:8px;align-self:flex-end;color:var(--white);font-weight:700;font-size:11px}
.follow i{width:22px;height:22px;background:var(--accent);display:inline-block}
.footer-bottom{position:absolute;bottom:0;left:0;right:0;height:32px;background:var(--footer-deep);font-size:10px;color:#8b938d}
.footer-bottom .container{display:flex;align-items:center;height:32px}
.chat{position:absolute;right:10px;bottom:0;background:var(--accent);color:var(--white);font-size:10px;font-weight:600;padding:8px 18px}
</style>
</head>
<body>

<header>
  <div class="topbar">
    <div class="container">
      <span><svg width="12" height="10" viewBox="0 0 12 10"><rect x=".5" y=".5" width="11" height="9" fill="none" stroke="#858b92"/><path d="M.5 .5 6 5 11.5 .5" fill="none" stroke="#858b92"/></svg>hello@birchwoodstays.com</span>
      <span><svg width="11" height="11" viewBox="0 0 24 24"><path d="M6 2l4 5-2 3a12 12 0 006 6l3-2 5 4-3 4C10 22 2 14 2 5z" fill="#858b92"/></svg>Call: 01632 960 418</span>
      <span>Log in</span>
    </div>
  </div>
  <nav class="site-nav">
    <div class="container">
      <a class="brand" href="#"><span class="mark"></span>Birchwood Stays</a>
      <div class="menu">
        <a class="active" href="#">Home</a>
        <a href="#">Caravans &amp; Lodges</a>
        <a href="#">Late Deals</a>
        <a href="#">Reviews</a>
        <a href="#">Holiday Parks</a>
        <a href="#">Information</a>
        <a href="#">Contact Us</a>
      </div>
    </div>
  </nav>
</header>

<section class="hero">
  <div class="hero-photo" role="img" aria-label="Lakeside holiday lodges with a wooden deck at sunset"></div>
  <div class="hero-content">
    <h1>Private Holiday Rentals</h1>
    <p>Caravans &amp; lodges to rent direct from owners across the UK's finest parks</p>
    <a class="btn" href="#">More Details</a>
  </div>
</section>

<form class="search-bar">
  <div class="search-field wide">Where do you want to go?</div>
  <div class="search-field">Check in <span>▾</span></div>
  <div class="search-field">Nights <span>▾</span></div>
  <div class="search-field">Guests <span>▾</span></div>
  <div class="search-field">Type <span>▾</span></div>
  <a class="btn" href="#">Search Now</a>
</form>

<section class="about">
  <div class="container">
    <div class="about-art" role="img" aria-label="Illustration of travel balloons, a plane and a suitcase"></div>
    <div class="about-text">
      <h2>About Us</h2>
      <h3>No deposit holidays</h3>
      <p>Would you like to book a little escape or a longer break at one of our lovely parks? Choose from our caravans and lodges and pay in easy stages.</p>
      <p>We have families on our books every month who return each year. Book with us and you can spread the cost with no deposit and no hidden fees, paying the balance before you arrive.</p>
      <a class="btn" href="#">Read More</a>
    </div>
  </div>
</section>

<section class="listings">
  <div class="container">
    <h2 class="section-title">List of caravans and lodges</h2>
    <div class="cards">
      <article class="card">
        <div class="card-photo" role="img" aria-label="Bright lodge interior with large windows" style="background:linear-gradient(135deg,#e9e2d6,#b9a791)"></div>
        <span class="price">£270.00</span>
        <div class="card-body">
          <h4>The Heronsgate</h4>
          <div class="addr">Heron Bay Holiday Park, Fernley, Kent</div>
          <div class="specs">
            <span>⌂ <b>Caravan</b></span><span>▣ <b>Lodge</b></span>
            <span>☺ Sleeps <b>6</b></span><span>◫ Beds <b>3</b></span>
          </div>
        </div>
      </article>
      <article class="card">
        <div class="card-photo" role="img" aria-label="Lodge living room with sofas" style="background:linear-gradient(135deg,#d9cbb7,#8c6f55)"></div>
        <span class="price">£270.00</span>
        <div class="card-body">
          <h4>The Willowdale</h4>
          <div class="addr">Heron Bay Holiday Park, Fernley, Kent</div>
          <div class="specs">
            <span>⌂ <b>Caravan</b></span><span>▣ <b>Lodge</b></span>
            <span>☺ Sleeps <b>6</b></span><span>◫ Beds <b>3</b></span>
          </div>
        </div>
      </article>
      <article class="card">
        <div class="card-photo" role="img" aria-label="Lodge bedroom with a double bed" style="background:linear-gradient(135deg,#e4d6c3,#a07a58)"></div>
        <span class="price">£270.00</span>
        <div class="card-body">
          <h4>The Ashbury</h4>
          <div class="addr">Heron Bay Holiday Park, Fernley, Kent</div>
          <div class="specs">
            <span>⌂ <b>Caravan</b></span><span>▣ <b>Lodge</b></span>
            <span>☺ Sleeps <b>6</b></span><span>◫ Beds <b>3</b></span>
          </div>
        </div>
      </article>
    </div>
    <div class="more"><a class="btn" href="#">View More Caravans</a></div>
  </div>
</section>

<section class="deals">
  <div class="container">
    <h2 class="section-title">Late Deals</h2>
    <div class="cards">
      <article class="card">
        <div class="card-photo" role="img" aria-label="Caravan hallway with wooden stairs" style="background:linear-gradient(135deg,#efe9df,#c3ad90)"></div>
        <div class="card-body">
          <h4>The Heronsgate</h4>
          <div class="date">Friday 04 September 2015 (3 nights)</div>
          <div class="specs"><span>⌂ <b>Caravan</b></span><span>▣ <b>Lodge</b></span><span>☺ Sleeps <b>6</b></span><span>◫ Beds <b>3</b></span></div>
          <a class="btn" href="#">Book Now for £199</a>
        </div>
      </article>
      <article class="card">
        <div class="card-photo" role="img" aria-label="Open plan lodge lounge" style="background:linear-gradient(135deg,#e2d3bd,#94735a)"></div>
        <div class="card-body">
          <h4>The Willowdale</h4>
          <div class="date">Friday 04 September 2015 (3 nights)</div>
          <div class="specs"><span>⌂ <b>Caravan</b></span><span>▣ <b>Lodge</b></span><span>☺ Sleeps <b>6</b></span><span>◫ Beds <b>3</b></span></div>
          <a class="btn" href="#">Book Now for £199</a>
        </div>
      </article>
      <article class="card">
        <div class="card-photo" role="img" aria-label="Cosy lodge bedroom" style="background:linear-gradient(135deg,#eadfcf,#a8825f)"></div>
        <div class="card-body">
          <h4>The Ashbury</h4>
          <div class="date">Friday 04 September 2015 (3 nights)</div>
          <div class="specs"><span>⌂ <b>Caravan</b></span><span>▣ <b>Lodge</b></span><span>☺ Sleeps <b>6</b></span><span>◫ Beds <b>3</b></span></div>
          <a class="btn" href="#">Book Now for £199</a>
        </div>
      </article>
    </div>
  </div>
</section>

<section class="reviews">
  <div class="container">
    <h2 class="section-title">Latest reviews</h2>
    <div class="tabs">
      <span class="active">Dana Fieldhouse</span><span>Maria Holt</span><span>Sam Reeves</span><span>Owen Tate</span><span>Lucy Marshall</span>
    </div>
    <div class="review">
      <div class="review-photo" role="img" aria-label="Photo of a happy guest giving a thumbs up"></div>
      <div class="review-text">
        <p>“Lovely lodge, spotless and well equipped. The children loved the pool and the lake walks. Booking was easy and the payment plan made it simple to plan our summer.”</p>
        <p class="who">Dana Fieldhouse</p>
        <div class="stars"><i></i><i></i><i></i><i></i><i></i></div>
      </div>
    </div>
  </div>
</section>

<section class="blog">
  <div class="container">
    <h2 class="section-title">Blog Feed</h2>
    <div class="cards">
      <article class="card">
        <div class="card-photo" role="img" aria-label="Lodge kitchen and dining area" style="background:linear-gradient(135deg,#e8ddd0,#9b7b5f)"></div>
        <div class="card-body">
          <h4>Top tips for a family lodge break</h4>
          <div class="meta">Posted by Birchwood Stays</div>
          <p class="excerpt">Planning your first caravan holiday? Here are our favourite ideas for packing light and keeping little ones happy.</p>
          <a class="read" href="#">Read more →</a>
        </div>
      </article>
      <article class="card">
        <div class="card-photo" role="img" aria-label="Bright lodge living room" style="background:linear-gradient(135deg,#f0e6d4,#b48f63)"></div>
        <div class="card-body">
          <h4>Top tips for a family lodge break</h4>
          <div class="meta">Posted by Birchwood Stays</div>
          <p class="excerpt">Planning your first caravan holiday? Here are our favourite ideas for packing light and keeping little ones happy.</p>
          <a class="read" href="#">Read more →</a>
        </div>
      </article>
      <article class="card">
        <div class="card-photo" role="img" aria-label="Modern lodge lounge interior" style="background:linear-gradient(135deg,#e4d8c6,#8f6d4f)"></div>
        <div class="card-body">
          <h4>Top tips for a family lodge break</h4>
          <div class="meta">Posted by Birchwood Stays</div>
          <p class="excerpt">Planning your first caravan holiday? Here are our favourite ideas for packing light and keeping little ones happy.</p>
          <a class="read" href="#">Read more →</a>
        </div>
      </article>
    </div>
  </div>
</section>

<footer class="site-footer">
  <div class="newsletter">
    <h3>Subscribe to our newsletter</h3>
    <div class="subscribe"><span class="input">your@email.com</span><a class="btn" href="#">Subscribe</a></div>
  </div>
  <div class="container">
    <div class="footer-cols">
      <div><h5>Corporate</h5><ul><li>Home</li><li>About Us</li><li>Jobs</li></ul></div>
      <div><h5>Students</h5><ul><li>How it Works</li><li>Find a Lodge</li><li>Register</li></ul></div>
      <div><h5>&nbsp;</h5><ul><li>Write For Us</li><li>Review Guidelines</li><li>Contact Us</li></ul></div>
      <div class="follow">FOLLOW US ON <i></i><i></i><i></i><i></i></div>
      <div><h5>Landlords</h5><ul><li>How it Works</li><li>Register</li></ul></div>
      <div><h5>Legal</h5><ul><li>Terms of Use</li><li>Privacy Policy</li><li>Disclaimer</li></ul></div>
    </div>
  </div>
  <div class="footer-bottom"><div class="container">© 2015 Birchwood Stays. All rights reserved.</div></div>
  <a class="chat" href="#">Leave a message</a>
</footer>

</body>
</html>
```